World domination merchandise

We need an illustration to print on a notebook (maybe eventually on other kinds of merchandise). We would like the words "Mes plans de domination mondiale" (which means "my world domination plans") in a calligraphy-like font, with maybe a world map, a globe, a flag... It has to be consistent with the vibe of our company, which is named "La Clairière" (The clearing). We are managing a community of entrepreneurs on a web-platform that is regrouping a forum and an online courses portal. Here are some keywords that represent our brand: vintage (in a modern way, if that makes sense), World War II, 40's/50's, entrepreneurship, web-marketing, community, sodality, collaboration.

I've attached a few image we like for inspiration

```html
<!DOCTYPE html>
<html lang="fr">
<head>
<meta charset="UTF-8">
<title>Mes plans de domination mondiale</title>
<link href="https://fonts.googleapis.com/css2?family=Great+Vibes&family=Uncial+Antiqua&family=Kaushan+Script&display=swap" rel="stylesheet">
<style>
  :root {
    --kraft: #c7a37b;
    --ink: #1b1511;
    --ink-soft: rgba(27, 21, 17, 0.78);
  }
  html, body {
    margin: 0;
    padding: 0;
    overflow: hidden;
  }
  .artboard {
    position: relative;
    width: 1175px;
    height: 1200px;
    background: var(--kraft);
    overflow: hidden;
    color: var(--ink);
  }
  .globe-mark {
    position: absolute;
    left: 555px;
    top: 150px;
    width: 110px;
    height: 150px;
  }
  .title-line {
    position: absolute;
    left: 0;
    width: 100%;
    margin: 0;
    text-align: center;
    line-height: 1;
    font-weight: 400;
  }
  .title-script {
    top: 255px;
    font-family: "Great Vibes", cursive;
    font-size: 170px;
  }
  .title-connector {
    top: 470px;
    font-family: "Great Vibes", cursive;
    font-size: 90px;
  }
  .title-uncial {
    top: 560px;
    font-family: "Uncial Antiqua", serif;
    font-size: 138px;
    letter-spacing: -2px;
  }
  .title-brush {
    top: 710px;
    font-family: "Kaushan Script", cursive;
    font-size: 190px;
    letter-spacing: -4px;
  }
  .flourish {
    position: absolute;
  }
  .flourish-left { left: 220px; top: 505px; width: 290px; height: 30px; }
  .flourish-right { left: 665px; top: 505px; width: 290px; height: 30px; }
  .flourish-star { left: 240px; top: 930px; width: 700px; height: 90px; }
</style>
</head>
<body>
  <main class="artboard">
    <svg class="globe-mark" role="img" aria-label="Small globe with a flag planted on top" viewBox="0 0 110 150">
      <rect x="53" y="0" width="4" height="52" fill="var(--ink)"/>
      <circle cx="55" cy="100" r="48" fill="var(--ink-soft)"/>
    </svg>

    <h1 class="title-line title-script">Mes plans</h1>

    <svg class="flourish flourish-left" role="img" aria-label="Decorative flourish" viewBox="0 0 290 30">
      <rect x="0" y="12" width="290" height="6" rx="3" fill="var(--ink-soft)"/>
    </svg>
    <p class="title-line title-connector">de</p>
    <svg class="flourish flourish-right" role="img" aria-label="Decorative flourish" viewBox="0 0 290 30">
      <rect x="0" y="12" width="290" height="6" rx="3" fill="var(--ink-soft)"/>
    </svg>

    <p class="title-line title-uncial">domination</p>
    <p class="title-line title-brush">Mondiale</p>

    <svg class="flourish flourish-star" role="img" aria-label="Curved swoosh flourish with a star" viewBox="0 0 700 90">
      <rect x="0" y="30" width="700" height="30" rx="15" fill="var(--ink-soft)"/>
    </svg>
  </main>
</body>
</html>
```